Book Cover for Christian book about open-air preaching

The book is about open-air or outdoor preaching. It is for pastors, evangelists, or any Christian who feels called to share the Gospel with crowds outside of the church. The title is "Quiet Meadows" with a subtitle of "A guide for patient gardening in the distant valley". The Bible verse reference for the title is Jeremiah 20:9. Size will be 9" high by 6"wide
Updates

Went on vacation/holiday

Target Market(s)

Christian pastors, missonaries, evangelists

Industry/Entity Type

religous

Requirements
Must have
• Meet Marlowe Indie Print Services guidelines for book covers

```html
<!DOCTYPE html>
<html lang="en">
<head>
<meta charset="utf-8">
<title>Quiet Meadows — Book Cover</title>
<link rel="stylesheet" href="https://fonts.googleapis.com/css2?family=Jost:wght@400;500&display=swap">
<style>
  :root {
    --page-bg: #e6e6e6;
    --paper: #efefef;
    --title-ink: #3a4247;
    --title-ink-soft: #55646f;
    --sky-mist: #dfe5ea;
    --sky-mid: #6d879e;
    --sky-light: #b4c4d2;
    --forest: #2b4852;
    --forest-snow: #8599a8;
    --wood: #5a4634;
    --wood-deep: #34291f;
    --light-ink: #f4f6f8;
  }
  * { margin: 0; padding: 0; box-sizing: border-box; }
  html, body {
    width: 1200px;
    height: 800px;
    overflow: hidden;
    background: var(--page-bg);
  }
  .stage {
    width: 1200px;
    height: 800px;
    display: flex;
    align-items: center;
    justify-content: center;
  }
  .cover {
    position: relative;
    width: 480px;
    height: 720px;
    overflow: hidden;
    background: var(--paper);
    font-family: "Jost", "Futura", sans-serif;
  }
  .cover-scene {
    position: absolute;
    inset: 0;
    background:
      radial-gradient(ellipse 55% 30% at 78% 50%, rgba(236,240,244,0.55) 0%, rgba(236,240,244,0) 100%),
      linear-gradient(to bottom,
        var(--paper) 0%,
        var(--paper) 27%,
        var(--sky-mist) 33%,
        var(--sky-mid) 42%,
        var(--sky-light) 56%,
        #7d93a6 64%,
        var(--forest) 74%,
        #4d6673 80%,
        var(--forest-snow) 85%,
        var(--wood) 92%,
        var(--wood-deep) 100%);
  }
  .cover-title {
    position: absolute;
    top: 80px;
    left: 0;
    right: 0;
    text-align: center;
    color: var(--title-ink);
    font-weight: 400;
    font-size: 90px;
    line-height: 90px;
    letter-spacing: 0.005em;
    text-transform: uppercase;
  }
  .cover-title .title-line { display: block; }
  .cover-title .title-line + .title-line { color: var(--title-ink-soft); }
  .cover-subtitle {
    position: absolute;
    top: 286px;
    left: 0;
    right: 0;
    text-align: center;
    color: var(--light-ink);
    font-size: 19px;
    line-height: 1.1;
    font-variant: small-caps;
    letter-spacing: 0.05em;
  }
  .cover-author {
    position: absolute;
    bottom: 12px;
    left: 0;
    right: 0;
    text-align: center;
    color: var(--light-ink);
    font-weight: 500;
    font-size: 16px;
    letter-spacing: 0.45em;
    text-transform: uppercase;
  }
</style>
</head>
<body>
  <main class="stage">
    <article class="cover">
      <div class="cover-scene" role="img" aria-label="Photograph of a cloudy winter sky over snow-covered pine forest, with a brown leather Bible resting on a wooden table in the foreground"></div>
      <h1 class="cover-title">
        <span class="title-line">Quiet</span>
        <span class="title-line">Meadows</span>
      </h1>
      <p class="cover-subtitle">A guide for patient gardening<br>in the distant valley</p>
      <p class="cover-author">Author Name</p>
    </article>
  </main>
</body>
</html>
```